Homepage für Immobilienmakler
Zielgruppe
Wir sind ein neuer und junger Immobilienmakler. Wir wollen moderne und neue Wege gehen. Damit meinen wir, extrem modern und auffallend professionell.
Unsere Immobilien sind von Anlegerwohnungen über Häuser bis hin zu Gewerbeimmobilien
Unsere Zielgruppe ist von jung bis alt quer durch.
Aufgabenstellung
Homepagegestalltung für unsere Immobilienmaklerei.
Persönlich gefällt mir sehr gut das schwarz-weiß, jedoch wirkt das dann eher zu dunkel nehme ich mal an. Sonst würde mir die Homepage in grün, wie die Farbe im Logo, gut gefallen. Eventuell in weißer Schrift. ABER, ICH ÜBERLASSE EUCH DIE DESIGNSFARBEN.
Mir hätte dieses Design sehr gut gefallen, eventuelll könnt ihr dieses umgestallten:
http://vorlagenhain.example/item/auto-dealer-car-dealer-html-template/full_screen_preview/7719034
Kein muss, wenn ihr etwas besseres habt, dann bin ich auch froh ;)
Eventuell etwas mit Bewegung auf der Homepage oder so wäre auch gut.
Unsere Homepage hat die Domain:
wohnraum-kontor.example
Das Foto von mir sollte auf der Homepage eingebaut werden.
Auf der Homepage sollen die Immobilien, die wir verkaufen und vermieten angeführt werden. Zudem sollte ersichtlich sein, dass wir Immobilien suchen, um diese zu verkaufen oder zu vermieten.

```html
<!DOCTYPE html>
<html lang="de">
<head>
<meta charset="utf-8">
<title>Wohnraum Kontor – Immobilien</title>
<link href="https://fonts.googleapis.com/css2?family=PT+Sans:wght@400;700&display=swap" rel="stylesheet">
<style>
:root{
  --ink:#222222;
  --dark:#252525;
  --green:#3fae49;
  --orange:#f7941d;
  --white:#ffffff;
  --text-dark:#1a1a1a;
  --muted:#cfcfcf;
}
*{box-sizing:border-box;margin:0;padding:0}
html,body{width:677px;height:1200px;overflow:hidden;background:var(--dark)}
body{font-family:"PT Sans",Arial,sans-serif;color:var(--white)}
.page{position:relative;width:677px;height:1200px;background:var(--dark);overflow:hidden}
.abs{position:absolute}

/* header */
.topbar{left:0;top:0;width:677px;height:36px;background:var(--ink)}
.brand{font-weight:700;color:var(--green);font-size:21px;letter-spacing:-.3px;line-height:1;white-space:nowrap}
.brand-top{left:147px;top:7px}
.social{display:flex;gap:6px}
.social span{display:block;width:18px;height:18px;border:2px solid var(--white);border-radius:50%}
.social-top{left:481px;top:10px}

.light{left:0;top:36px;width:677px;height:294px;background:var(--white)}
.nav{display:flex;align-items:center;height:16px;font-size:6px;font-weight:700}
.nav a{color:var(--text-dark);text-decoration:none;position:absolute;top:4px}
.nav a.active{background:var(--green);color:var(--white);left:148px;top:0;width:24px;height:16px;display:flex;align-items:center;justify-content:center}
.nav-top{left:0;top:36px;width:677px}

/* hero */
.hero-photo{left:149px;top:76px;width:278px;height:192px;background:linear-gradient(180deg,#c9ced2 0%,#a9abab 30%,#7a7570 65%,#4a4744 85%,#6b6865 100%)}
.hero-caption{left:148px;top:268px;width:280px;height:41px;background:var(--ink);padding:2px 6px;font-size:7.6px;line-height:10px}
.hero-caption b{display:block}
.hero-caption .details,.card .details{color:var(--green);font-size:5px;line-height:6px;display:block}
.price{position:absolute;right:4px;top:5px;color:var(--orange);font-weight:700;font-size:14px}
.tag{background:var(--green);color:var(--white);font-weight:700;font-size:6.5px;padding:3px 5px;transform:rotate(-17deg);box-shadow:1px 1px 2px rgba(0,0,0,.25);white-space:nowrap}
.tag-new{left:421px;top:94px}
.teaser{left:438px;top:196px;color:var(--text-dark);font-size:15px;line-height:17.3px}
.teaser a{display:block;color:var(--green);font-size:7px;line-height:10px;margin-top:4px;text-decoration:none}

/* search */
.heading{color:var(--green);font-size:15px;line-height:18px}
.h-filter{left:147px;top:349px}
.field-col{width:88px}
.lbl{background:var(--green);font-weight:700;font-size:9px;height:16px;line-height:16px;padding-left:9px}
.sel{background:var(--white);color:var(--text-dark);font-weight:700;font-size:9px;height:14px;line-height:14px;padding-left:9px;position:relative}
.sel.caret::after{content:"";position:absolute;right:6px;top:6px;border:3px solid transparent;border-top:3px solid var(--text-dark)}
.search-btn{left:436px;top:416px;width:87px;height:15px;background:var(--orange);font-weight:700;font-size:9px;line-height:15px;padding-left:9px}
.search-btn svg{position:absolute;right:10px;top:-6px}

/* results */
.h-results{left:147px;top:461px}
.card{top:483px;width:87px;height:226px;background:var(--white);color:var(--text-dark);font-size:7.5px;line-height:10px}
.card .thumb{height:68px}
.card .body{padding:6px 2px 0}
.card b{display:block}
.card p{margin-bottom:10px}
.pager{left:498px;top:713px;font-size:4.5px;color:var(--muted)}

/* offer */
.h-offer{left:146px;top:739px}
.offer-text{left:146px;top:760px;width:382px;font-size:10px;line-height:12.2px}
.tag-wanted{left:405px;top:816px;font-size:10px;padding:4px 9px;transform:rotate(-13deg)}

/* contact */
.portrait{left:396px;top:876px;width:154px;height:324px;background:radial-gradient(ellipse at 50% 40%,#e8e4e0 0%,#c9b8a8 35%,#3a3838 80%,var(--dark) 100%);border-radius:40% 40% 0 0}
.call{left:149px;top:963px;font-size:14px;color:var(--green)}
.phone{left:147px;top:983px;font-size:25px;font-weight:700;color:var(--green);letter-spacing:.5px}
.brand-foot{left:147px;top:1022px}
.nav-foot{left:0;top:1179px;width:677px}
.nav-foot a{color:var(--white)}
.social-foot{left:481px;top:1174px}
</style>
</head>
<body>
<div class="page">
  <header class="abs topbar"></header>
  <div class="abs brand brand-top">Wohnraum Kontor</div>
  <div class="abs social social-top" aria-label="Soziale Netzwerke"><span></span><span></span></div>

  <div class="abs light"></div>
  <nav class="abs nav nav-top">
    <a class="active" href="#">Home</a>
    <a href="#" style="left:195px">Über uns</a>
    <a href="#" style="left:236px">Katalog</a>
    <a href="#" style="left:280px">Verkaufen</a>
    <a href="#" style="left:328px">FAQ</a>
    <a href="#" style="left:363px">Kontakt</a>
    <a href="#" style="left:407px">Blog</a>
  </nav>

  <div class="abs hero-photo" role="img" aria-label="Foto eines modernen grauen Würfelhauses mit Carport"></div>
  <div class="abs hero-caption">
    <b>Lorem ipsum</b>
    dolor sit amet, consetetur sadipscing elitr<br>
    Diam nonumy eirmod tempor invidunt ut labore
    <span class="details">Details</span>
    <span class="price">300.000$</span>
  </div>
  <div class="abs tag tag-new">Neues Angebot!</div>
  <div class="abs teaser">Neugierig?<br>Informieren<br>Sie sich<br>in unserem<br>aktuellen<br>Katalog!<a href="#">Hier gehts zum Katalog</a></div>

  <h2 class="abs heading h-filter">Ihre Auswahlhilfe</h2>
  <div class="abs field-col" style="left:148px;top:370px">
    <div class="lbl">Kaufen/Mieten</div><div class="sel caret">Alle</div>
    <div class="lbl">Immobilienart</div><div class="sel caret" style="height:15px">Alle</div>
  </div>
  <div class="abs field-col" style="left:244px;top:370px">
    <div class="lbl">Postleitzahl</div><div class="sel" style="height:16px"></div>
    <div class="lbl" style="height:14px;line-height:14px">Ort</div><div class="sel caret" style="height:15px">Alle</div>
  </div>
  <div class="abs field-col" style="left:340px;top:370px">
    <div class="lbl">Umkreis</div><div class="sel caret">Alle</div>
    <div class="lbl">max. Preis</div><div class="sel caret" style="height:15px">Alle</div>
  </div>
  <div class="abs search-btn">Suche
    <svg width="16" height="20" viewBox="0 0 16 20"><path d="M8 1a7 7 0 0 0-7 7c0 5 7 11 7 11s7-6 7-11a7 7 0 0 0-7-7z" fill="#fff"/><circle cx="8" cy="8" r="3.5" fill="var(--orange)"/></svg>
  </div>

  <h2 class="abs heading h-results">Ihr Suchergebnis</h2>
  <svg class="abs" style="left:129px;top:578px" width="12" height="18" viewBox="0 0 12 18"><path d="M10 1 2 9l8 8" fill="none" stroke="#fff" stroke-width="1.5"/></svg>
  <svg class="abs" style="left:530px;top:583px" width="12" height="18" viewBox="0 0 12 18"><path d="M2 1l8 8-8 8" fill="none" stroke="#fff" stroke-width="1.5"/></svg>

  <article class="abs card" style="left:148px">
    <div class="thumb" role="img" aria-label="Foto eines hellen Treppenhauses" style="background:linear-gradient(180deg,#8f9a66,#c9cbb8 60%,#e6e6e2)"></div>
    <div class="body"><p><b>Lorem ipsum</b>dolor sit amet, consetetur sadipscing elitr</p><p><b>Diam nonumy</b>eirmod tempor invidunt ut labore et dolore magna aliquyam erat</p><b>Ed diam</b>At vero eos et accusam et justo duo dolores<span class="details">Details</span></div>
  </article>
  <article class="abs card" style="left:244px">
    <div class="thumb" role="img" aria-label="Foto einer weißen Villa mit Rasen" style="background:linear-gradient(180deg,#5f93c9,#dfe2e2 55%,#6f9a3a)"></div>
    <div class="body"><p><b>Lorem ipsum</b>dolor sit amet, consetetur sadipscing elitr</p><p><b>Diam nonumy</b>eirmod tempor invidunt ut labore et dolore magna aliquyam erat</p><b>Ed diam</b>At vero eos et accusam et justo duo dolores<span class="details">Details</span></div>
  </article>
  <article class="abs card" style="left:339px">
    <div class="thumb" role="img" aria-label="Foto einer Häuserzeile mit bunten Fenstern" style="background:linear-gradient(180deg,#c8d2da,#b7bba6 55%,#6e6a44)"></div>
    <div class="body"><p><b>Lorem ipsum</b>dolor sit amet, consetetur sadipscing elitr</p><p><b>Diam nonumy</b>eirmod tempor invidunt ut labore et dolore magna aliquyam erat</p><b>Ed diam</b>At vero eos et accusam et justo duo dolores<span class="details">Details</span></div>
  </article>
  <article class="abs card" style="left:435px">
    <div class="thumb" role="img" aria-label="Foto eines grauen Würfelhauses" style="background:linear-gradient(180deg,#c9ced2,#7a7570 60%,#5a5754)"></div>
    <div class="body"><p><b>Lorem ipsum</b>dolor sit amet, consetetur sadipscing elitr</p><p><b>Diam nonumy</b>eirmod tempor invidunt ut labore et dolore magna aliquyam erat</p><b>Ed diam</b>At vero eos et accusam et justo duo dolores<span class="details">Details</span></div>
  </article>
  <div class="abs pager">1 | 2 | 3 | 4</div>

  <h2 class="abs heading h-offer">Sie möchten uns eine Immobilie anbieten?</h2>
  <p class="abs offer-text">Lorem ipsum dolor sit amet, consetetur sadipscing elitr, sed diam nonumy eirmod tempor invidunt ut labore et dolore magna aliquyam erat, sed diam voluptua. At vero eos et accusam et justo duo dolores et ea rebum. Stet clita kasd gubergren, no sea takimata sanctus est Lorem ipsum dolor sit amet. Lorem ipsum dolor sit amet, consetetur sadipscing elitr, sed diam nonumy eirmod tempor invidunt ut labore et</p>
  <div class="abs tag tag-wanted">Wir suchen ständig Immobilien!</div>

  <div class="abs portrait" role="img" aria-label="Foto des Maklers im weißen Poloshirt mit Laptoptasche"></div>
  <div class="abs call">Sprechen Sie mich an!</div>
  <div class="abs phone">030-55501234</div>
  <div class="abs brand brand-foot">Wohnraum Kontor</div>

  <nav class="abs nav nav-foot">
    <a href="#" style="left:152px">Home</a>
    <a href="#" style="left:195px">Über uns</a>
    <a href="#" style="left:236px">Katalog</a>
    <a href="#" style="left:280px">Verkaufen</a>
    <a href="#" style="left:328px">FAQ</a>
    <a href="#" style="left:363px">Kontakt</a>
  </nav>
  <div class="abs social social-foot" aria-label="Soziale Netzwerke"><span></span><span></span></div>
</div>
</body>
</html>
```